We are a doctors medical practice
I need the business card to be eye catching and memorable,
to reflect professionalism, yet also warmth and care

the numbers need to be easy to see, for the elderly

and the logo also in a location that is large enough to see and be eye catching

Back of card:
opening hours:
Mon- Fri 8.30am to 6pm
Sat 9am to 4pm

rows for appontments, date and time
Updates

HiĀ 

Modification to company name

BRAMBLEWOOD HOME HEALTH MEDICAL PRACTICE

Thanks
Clara

Reason: I am look for a unique design that also fulfils the design brief

I have attempted to post a .eps and .ai file of the logo

Target Market(s)

needs to appeal to the majority, mainly adults

Industry/Entity Type

Medical

Contact Information for Business Card

company name: Bramblewood Home Health Medical Practice
Name: Dr Clara Ostrowski-Vey
Qualifications: MBBS, Bsci(med), FRACGP, DCH, SH&FPA, Dip Derm
Address: Shop 3/41-43 Calder Rd, Brookvale 2371
Ph: 02 9418 3052
Fax: 02 9436 8120

Requirements
Nice to have
• I like balance
gold/ silver incorporated, as well as the other colours in the logo- but not limited to these colours
a "medical" feel
Should not have
• dark or strong colours

```html
<!DOCTYPE html>
<html lang="en">
<head>
<meta charset="utf-8">
<title>Bramblewood Home Health Medical Practice – Business Card</title>
<link rel="stylesheet" href="https://fonts.googleapis.com/css2?family=Open+Sans:wght@400;600;700&display=swap">
<style>
  :root {
    --page: #ffffff;
    --card-deep: #0a62b8;
    --card-mid: #1677cf;
    --card-light: #2a8fe3;
    --text-light: #ffffff;
    --accent-gold: #f3d21c;
    --mark-ring: #2a9be8;
    --mark-fill: #1b7fd3;
    --ghost-ring: rgba(120, 200, 255, 0.35);
    --ghost-fill: rgba(110, 190, 250, 0.18);
  }
  * { margin: 0; padding: 0; box-sizing: border-box; }
  html, body {
    width: 960px;
    height: 1200px;
    overflow: hidden;
    background: var(--page);
    font-family: "Open Sans", Arial, sans-serif;
  }
  .sheet { position: relative; width: 960px; height: 1200px; }
  .card {
    position: absolute;
    left: 46px;
    width: 870px;
    height: 525px;
    overflow: hidden;
    color: var(--text-light);
  }
  .card-front { top: 55px; }
  .card-back { top: 620px; }
  .card-surface {
    position: absolute;
    inset: 0;
    background: radial-gradient(ellipse at 50% 40%, var(--card-light) 0%, var(--card-mid) 45%, var(--card-deep) 100%);
  }
  .brand-mark {
    position: absolute;
    left: 308px;
    top: 90px;
    width: 254px;
    height: 254px;
  }
  .brand-name {
    position: absolute;
    left: 0;
    right: 0;
    top: 432px;
    text-align: center;
    font-weight: 700;
    font-size: 35px;
    letter-spacing: 0.5px;
    color: var(--text-light);
  }
  .ghost-mark {
    position: absolute;
    left: 30px;
    top: 10px;
    width: 440px;
    height: 420px;
  }
  .doctor {
    position: absolute;
    right: 42px;
    top: 150px;
    text-align: right;
  }
  .doctor-name {
    font-weight: 600;
    font-size: 40px;
    line-height: 1.1;
  }
  .doctor-qualifications {
    margin-top: 14px;
    font-size: 23px;
    line-height: 1.4;
  }
  .contact-address {
    position: absolute;
    left: 36px;
    top: 400px;
    display: flex;
    gap: 10px;
    font-weight: 700;
    font-size: 33px;
    line-height: 1.2;
  }
  .contact-lines {
    position: absolute;
    left: 504px;
    top: 396px;
    font-weight: 700;
    font-size: 40px;
    line-height: 1.15;
  }
  .contact-line { display: flex; align-items: center; gap: 14px; }
  .icon { flex: none; }
</style>
</head>
<body>
<main class="sheet">
  <section class="card card-front">
    <div class="card-surface" role="img" aria-label="Blue background with soft diamond pattern"></div>
    <svg class="brand-mark" viewBox="0 0 254 254" aria-hidden="true">
      <circle cx="127" cy="127" r="120" fill="var(--mark-fill)" stroke="var(--mark-ring)" stroke-width="8"/>
    </svg>
    <h1 class="brand-name">BRAMBLEWOOD HOME HEALTH MEDICAL</h1>
  </section>

  <section class="card card-back">
    <div class="card-surface" role="img" aria-label="Blue background with soft diamond pattern"></div>
    <svg class="ghost-mark" viewBox="0 0 440 420" aria-hidden="true">
      <circle cx="215" cy="225" r="190" fill="var(--ghost-fill)" stroke="var(--ghost-ring)" stroke-width="14"/>
    </svg>

    <div class="doctor">
      <h2 class="doctor-name">Dr Clara Ostrowski-Vey</h2>
      <p class="doctor-qualifications">MBBS, Bsci(med), FRACGP, DCH,<br>SH&amp;FPA, Dip Derm</p>
    </div>

    <address class="contact-address" style="font-style:normal">
      <svg class="icon" width="20" height="28" viewBox="0 0 20 28" aria-hidden="true" style="margin-top:6px">
        <path d="M10 0C4.5 0 0 4.4 0 9.8 0 17 10 28 10 28s10-11 10-18.2C20 4.4 15.5 0 10 0zm0 14a4.2 4.2 0 1 1 0-8.4 4.2 4.2 0 0 1 0 8.4z" fill="var(--accent-gold)"/>
      </svg>
      <span>Shop 3/41-43 Calder Rd,<br>Brookvale 2371</span>
    </address>

    <div class="contact-lines">
      <p class="contact-line">
        <svg class="icon" width="26" height="30" viewBox="0 0 26 30" aria-hidden="true">
          <path d="M6 2l5 6-3 4c2 4 5 7 8 9l4-3 5 5-4 5C12 27 3 16 1 6z" fill="none" stroke="var(--accent-gold)" stroke-width="3" stroke-linejoin="round"/>
        </svg>
        <span>[02] 9418 3052</span>
      </p>
      <p class="contact-line">
        <svg class="icon" width="28" height="28" viewBox="0 0 28 28" aria-hidden="true">
          <g fill="none" stroke="var(--accent-gold)" stroke-width="2.6">
            <rect x="7" y="2" width="14" height="9"/>
            <rect x="2" y="11" width="24" height="14" rx="2"/>
            <line x1="7" y1="19" x2="21" y2="19"/>
          </g>
        </svg>
        <span>[02] 9436 8120</span>
      </p>
    </div>
  </section>
</main>
</body>
</html>
```